Lumen Cove Skincare - Package Design

New Beauty label needing product packaging design. Looking for elegant and stylish design to represent our premium brand.

This project is for 1 label and 1 box design. The winning designer will be assigned another project for the next product in the range. (to be paid as a new project)

This product is for "Dead Sea Mud Mask". Please see the label format and jar attached. Please note there are 2 different jars we are considering (will have a mud inside). Please feel free to choose whichever one suits your design best.

The labels and boxes are to retain the product information, such as size, ingredients etc, but is to be updated to our brand. You can move or display the other information as you wish.

the size of the dead sea mud mask color box is 72*72*85mm (length*width*height)
the size of dead sea mud mask label is 218*58mm (width*height)

Target Market(s)

Women 15 to 65

Requirements
Must have
• Must be elegant and represent our brand which is a premium beauty product.
Should not have
• Dark blue. Dark purple etc. Colours should compliment the logo

```html
<!DOCTYPE html>
<html lang="en">
<head>
<meta charset="UTF-8">
<title>Lumen Cove Skincare – Packaging</title>
<link href="https://fonts.googleapis.com/css2?family=Great+Vibes&family=PT+Sans:ital,wght@0,400;1,400&display=swap" rel="stylesheet">
<style>
  :root {
    --page: #ffffff;
    --panel: #0e0e0e;
    --panel-edge: #262626;
    --gold: #d9a92e;
    --gold-light: #f3d77a;
    --gold-dark: #a8791a;
    --ink-light: #f4f1ea;
    --ink-muted: #b9b4a8;
  }
  * { box-sizing: border-box; margin: 0; padding: 0; }
  html, body { width: 1200px; height: 1200px; overflow: hidden; background: var(--page); }
  .canvas { position: relative; width: 1200px; height: 1200px; }

  .panel {
    position: absolute;
    background: var(--panel);
    border: 1px solid var(--panel-edge);
    color: var(--ink-light);
    font-family: "PT Sans", sans-serif;
    overflow: hidden;
  }

  /* Box top panel */
  .box-top { left: 590px; top: 40px; width: 300px; height: 300px; display: flex; align-items: center; justify-content: center; }
  .box-top .brand-name { font-size: 15px; letter-spacing: 3px; }

  /* Box side panel */
  .box-side { left: 290px; top: 340px; width: 300px; height: 355px; padding: 34px 26px; }
  .box-side .brand-name { font-size: 13px; letter-spacing: 3px; margin-bottom: 26px; }
  .info-block { margin-bottom: 16px; }
  .info-block h3 { font-weight: 400; font-size: 12px; color: var(--gold); margin-bottom: 3px; }
  .info-block p { font-size: 11px; color: var(--ink-muted); line-height: 1.4; }

  /* Box front panel */
  .box-front { left: 590px; top: 340px; width: 300px; height: 355px; display: flex; flex-direction: column; align-items: center; padding: 70px 16px 0; }

  /* Jar label */
  .jar-label { left: 50px; top: 770px; width: 1100px; height: 293px; display: flex; flex-direction: column; align-items: center; padding-top: 40px; }

  .brand-lockup { display: flex; align-items: center; gap: 10px; }
  .brand-dot { width: 8px; height: 8px; border-radius: 50%; background: var(--gold); flex: none; }
  .brand-name { font-family: "PT Sans", sans-serif; font-weight: 400; color: var(--gold); text-transform: uppercase; white-space: nowrap; }
  .box-front .brand-name { font-size: 15px; letter-spacing: 3px; }
  .jar-label .brand-name { font-size: 26px; letter-spacing: 5px; }
  .jar-label .brand-dot { width: 10px; height: 10px; }

  .headline { font-family: "Great Vibes", cursive; font-weight: 400; color: var(--ink-light); white-space: nowrap; }
  .headline .accent { color: var(--gold); }
  .box-front .headline { font-size: 34px; margin-top: 58px; }
  .jar-label .headline { font-size: 50px; margin-top: 26px; }

  .feature-bar {
    display: flex;
    background: linear-gradient(90deg, var(--gold-dark), var(--gold-light) 50%, var(--gold));
  }
  .feature-bar span { font-style: italic; color: #2a1f08; white-space: nowrap; border-right: 1px solid rgba(0,0,0,0.25); }
  .feature-bar span:last-child { border-right: none; }
  .box-front .feature-bar { margin-top: 6px; }
  .box-front .feature-bar span { font-size: 11px; padding: 2px 7px; }
  .jar-label .feature-bar { margin-top: 8px; }
  .jar-label .feature-bar span { font-size: 14px; padding: 4px 12px; }

  .tagline { font-style: italic; text-align: center; color: var(--ink-light); line-height: 1.35; }
  .box-front .tagline { font-size: 10.5px; margin-top: 16px; }
  .jar-label .tagline { font-size: 13px; margin-top: 22px; }
</style>
</head>
<body>
<div class="canvas">

  <section class="panel box-top">
    <div class="brand-lockup">
      <span class="brand-dot"></span>
      <span class="brand-name">Lumen Cove Skincare</span>
    </div>
  </section>

  <section class="panel box-side">
    <div class="brand-name">Lumen Cove Skincare</div>
    <div class="info-block">
      <h3>Lorem Ipsum</h3>
      <p>Mineral-rich mud gently draws out impurities.</p>
    </div>
    <div class="info-block">
      <h3>Lorem Ipsum</h3>
      <p>Apply a thin layer to clean, dry skin.</p>
    </div>
    <div class="info-block">
      <h3>Lorem Ipsum</h3>
      <p>Leave for ten minutes, then rinse with warm water.</p>
    </div>
    <div class="info-block">
      <h3>Lorem Ipsum</h3>
      <p>Store in a cool, dry place away from sunlight.</p>
    </div>
  </section>

  <section class="panel box-front">
    <div class="brand-lockup">
      <span class="brand-dot"></span>
      <span class="brand-name">Lumen Cove Skincare</span>
    </div>
    <h1 class="headline">What is Lorem <span class="accent">Ipsum</span></h1>
    <div class="feature-bar">
      <span>Lorem Ipsum</span><span>Lorem Ipsum</span><span>Lorem Ipsum</span>
    </div>
    <p class="tagline">Lorem Ipsum is simply dummy text of the printing and<br>typesetting industry.</p>
  </section>

  <section class="panel jar-label">
    <div class="brand-lockup">
      <span class="brand-dot"></span>
      <span class="brand-name">Lumen Cove Skincare</span>
    </div>
    <h2 class="headline">What is Lorem <span class="accent">Ipsum</span></h2>
    <div class="feature-bar">
      <span>Lorem Ipsum</span><span>Lorem Ipsum</span><span>Lorem Ipsum</span>
    </div>
    <p class="tagline">Lorem Ipsum is simply dummy text of the printing and<br>typesetting industry.</p>
  </section>

</div>
</body>
</html>
```